Business Card Design - Carrington Hill Lodge

We are looking at a new design for our business cards that has a modern and professional look. We run a residential aged care facility focussing on the care of residents. The cards will be used for potential clients, consultants and business opportunities in this sector. Blue and white is our main colours and would to see these colours incorporated in the design.
Industry/Entity Type
Business
Contact Information for Business Card
Carrington Hill Lodge, Darren Pelham, dpelham@carringtonhilllodge.com.au, Finance Manager, 0491 736 208, Unit 3, 48 Yarrabee Way, Brookvale Park, Qld 4215.

```html
<!DOCTYPE html>
<html lang="en">
<head>
<meta charset="utf-8">
<title>Carrington Hill Lodge – Business Card</title>
<link rel="stylesheet" href="https://fonts.googleapis.com/css2?family=Oswald:wght@300;400&family=Open+Sans:wght@400&display=swap">
<style>
  :root {
    --backdrop: #8a8a8a;
    --lodge-blue: #4e7b95;
    --wave-edge: #a9c2cf;
    --card-white: #ffffff;
    --ink-dark: #222222;
    --ink-navy: #213d4c;
  }
  * { margin: 0; padding: 0; box-sizing: border-box; }
  html, body { width: 1200px; height: 1000px; overflow: hidden; }
  body { background: var(--backdrop); position: relative; font-family: "Open Sans", sans-serif; }

  .card { position: absolute; width: 525px; height: 324px; overflow: hidden; }
  .card-front { left: 528px; top: 150px; background: var(--card-white); }
  .card-back { left: 147px; top: 525px; background: var(--lodge-blue); }

  .card-wave { position: absolute; inset: 0; width: 525px; height: 324px; }

  .brand-mark { position: absolute; display: flex; flex-direction: column; align-items: center; }
  .brand-dot { display: block; border-radius: 50%; }
  .brand-name {
    font-family: "Oswald", sans-serif; font-weight: 400; color: var(--ink-navy);
    letter-spacing: .5px; text-transform: uppercase; white-space: nowrap; line-height: 1;
  }
  .card-front .brand-mark { left: 40px; top: 38px; width: 140px; }
  .card-front .brand-dot { width: 76px; height: 76px; background: var(--lodge-blue); }
  .card-front .brand-name { font-size: 12px; margin-top: 8px; }

  .card-back .brand-mark { left: 0; width: 525px; top: 74px; }
  .card-back .brand-dot { width: 120px; height: 120px; background: var(--card-white); }
  .card-back .brand-name { font-size: 24px; margin-top: 14px; }

  .holder { position: absolute; right: 61px; top: 44px; text-align: right; font-family: "Oswald", sans-serif; color: var(--ink-dark); }
  .holder-name { font-size: 28px; font-weight: 400; line-height: 1.1; letter-spacing: .5px; }
  .holder-role { font-size: 19px; font-weight: 300; line-height: 1.1; letter-spacing: .5px; }

  .contact { position: absolute; left: 256px; top: 181px; list-style: none; color: var(--card-white); font-size: 13px; line-height: 17px; }
  .contact li { display: flex; gap: 12px; margin-bottom: 9px; }
  .contact svg { width: 12px; height: 12px; flex: none; margin-top: 2px; fill: var(--card-white); }
</style>
</head>
<body>

<section class="card card-front" aria-label="Business card front">
  <svg class="card-wave" viewBox="0 0 525 324" aria-hidden="true">
    <path d="M-6,126 Q20,118 38,136 A76,70 0 0 0 180,160 L186,150 Q196,136 214,134 Q236,130 256,134 Q266,138 274,130 Q284,124 296,132 Q306,140 316,130 Q328,122 340,132 Q350,140 362,130 Q376,122 390,132 Q400,140 412,130 Q426,122 440,132 Q452,140 464,130 Q478,122 490,132 Q504,140 531,128 L531,330 L-6,330 Z"
          fill="var(--lodge-blue)" stroke="var(--wave-edge)" stroke-width="3"/>
  </svg>

  <div class="brand-mark">
    <span class="brand-dot"></span>
    <span class="brand-name">Carrington Hill Lodge</span>
  </div>

  <div class="holder">
    <p class="holder-name">DARREN PELHAM</p>
    <p class="holder-role">FINANCE MANAGER</p>
  </div>

  <ul class="contact">
    <li>
      <svg viewBox="0 0 12 12"><path d="M6 1 L11.5 6 L10 6 L10 11 L7.5 11 L7.5 8 L4.5 8 L4.5 11 L2 11 L2 6 L0.5 6 Z"/></svg>
      <span>Carrington Hill Lodge<br>Unit 3, 48 Yarrabee Way<br>Brookvale Park, Qld 4215</span>
    </li>
    <li>
      <svg viewBox="0 0 12 12"><path d="M2.5 0.8 L4.5 3.2 L3.4 4.6 Q4.6 7.2 7.4 8.6 L8.8 7.5 L11.2 9.5 L10 11.2 Q4 11 0.8 2 Z"/></svg>
      <span>0491 736 208</span>
    </li>
    <li>
      <svg viewBox="0 0 12 12"><path d="M0.5 2.5 H11.5 V3.4 L6 6.8 L0.5 3.4 Z M0.5 4.6 L6 8 L11.5 4.6 V10 H0.5 Z"/></svg>
      <span>dpelham@carringtonhilllodge.com.au</span>
    </li>
  </ul>
</section>

<section class="card card-back" aria-label="Business card back">
  <div class="brand-mark">
    <span class="brand-dot"></span>
    <span class="brand-name">Carrington Hill Lodge</span>
  </div>
</section>

</body>
</html>
```